Brochure Design Project for Home Watch company

We are a new start up company in fast growing home watch industry. We provide services in Hawaii so the design needs to be reflect that. Our web site can give you overview of what we do - www.palmcrestkeeper.com. We will service clients that own second homes in Hawaii. These properties are not necessarily income producing properties for our clients. I'm looking for 2 or 4 page brochure which will be used to market our services to potential new clients. It needs to be high quality, modern with slight Hawaiian feel (we are based on Oahu). I'm not looking for a trifold type of brochure.

We are open to various colors based on what the designer might suggest but as you can see on our home page - the main picture of the home on our site has lots of red and white which we like as well as the "head" or dot above the "i" in our logo is red. I was not able to upload the file of the main house (purchased on snapvaultpix) on here therefore I'll have to provide the original photo to the selected designer at the later time. For now I just uploaded the not purchased copy.

If you have other questions please do let me know. And lastly, I will be looking to create a business card and post card as well.

```html
<!DOCTYPE html>
<html lang="en">
<head>
<meta charset="utf-8">
<title>Palm Crest Keeper Brochure</title>
<link rel="stylesheet" href="https://fonts.googleapis.com/css2?family=Montserrat:wght@600;700&family=Oswald:wght@500;600&family=Roboto+Condensed:wght@400&display=swap">
<style>
:root{
  --red:#ef5557;
  --black:#0d0d0d;
  --ink:#222;
  --muted:#555;
  --white:#fff;
  --sky:#6fa8d8;
  --sea:#2f8fb5;
  --green:#5d7a3e;
}
*{margin:0;padding:0;box-sizing:border-box}
html,body{width:1200px;height:941px;overflow:hidden;background:var(--white)}
.stage{position:absolute;left:0;top:0;width:1500px;height:1176px;transform:scale(.8);transform-origin:0 0}
.page{position:absolute;width:652px;height:915px;background:var(--white);box-shadow:0 2px 10px rgba(0,0,0,.25);overflow:hidden;font-family:"Roboto Condensed",sans-serif;color:var(--ink)}
.page--front{left:78px;top:141px}
.page--back{left:788px;top:141px;width:654px;height:917px}
.page svg.shapes{position:absolute;left:0;top:0}
.abs{position:absolute}
.brand{display:flex;align-items:center;gap:10px}
.brand__dot{width:16px;height:16px;border-radius:50%;background:var(--red)}
.brand__name{font-family:"Oswald",sans-serif;font-weight:600;font-size:24px;line-height:1.05;color:var(--black);width:110px}
.brand__tag{font-family:"Roboto Condensed",sans-serif;font-size:15px;color:var(--muted);margin-top:6px}
.headline{font-family:"Montserrat",sans-serif;font-weight:700;color:var(--black)}
.headline--lg{font-size:34px}
.headline--md{font-size:25px}
.headline__accent{font-family:"Oswald",sans-serif;font-weight:600;font-size:32px;color:var(--red);letter-spacing:.3px;line-height:1.1}
.pill{position:absolute;left:0;height:24px;background:var(--black);color:var(--red);font-family:"Oswald",sans-serif;font-weight:500;font-size:17px;line-height:24px;padding-left:22px;border-radius:0 12px 12px 0}
.body{font-size:10.6px;line-height:1.22;text-align:justify;color:var(--ink)}
.subhead{font-family:"Oswald",sans-serif;font-weight:500;font-size:19px;color:var(--red)}
.title-black{font-family:"Oswald",sans-serif;font-weight:600;font-size:25px;color:var(--black);line-height:1.2}
.title-red{font-family:"Oswald",sans-serif;font-weight:600;font-size:25px;color:var(--red);line-height:1.2}
.contact__name{font-family:"Oswald",sans-serif;font-weight:500;font-size:18px;color:var(--red);margin-bottom:6px}
.contact__line{display:flex;align-items:center;gap:6px;font-family:"Montserrat",sans-serif;font-weight:600;font-size:13.5px;line-height:22px}
.contact--dark .contact__line{color:var(--white)}
.contact--light .contact__line{color:var(--ink);font-weight:600}
.photo{position:absolute}
</style>
</head>
<body>
<div class="stage">

  <!-- FRONT PAGE -->
  <section class="page page--front">
    <svg class="shapes" width="652" height="915" viewBox="0 0 652 915">
      <defs>
        <linearGradient id="villa" x1="0" y1="0" x2="0" y2="1">
          <stop offset="0" stop-color="#4f8fd0"/>
          <stop offset=".45" stop-color="#9cc4e6"/>
          <stop offset=".62" stop-color="#8a6a55"/>
          <stop offset=".8" stop-color="#d8d8d4"/>
          <stop offset="1" stop-color="#2d7fa6"/>
        </linearGradient>
      </defs>
      <path role="img" aria-label="Photo of a Hawaiian villa with infinity pool overlooking the ocean" d="M0 255 L400 22 L652 210 L652 462 Q330 440 0 478 Z" fill="url(#villa)"/>
      <path d="M0 255 L400 22 L652 210 L652 240 L400 60 Q200 170 0 285 Z" fill="var(--red)"/>
      <rect x="530" y="92" width="46" height="90" fill="var(--red)"/>
      <path d="M530 92 L578 92" stroke="var(--black)" stroke-width="5"/>
      <path d="M0 252 L400 14 L652 200" fill="none" stroke="var(--black)" stroke-width="5"/>
      <path d="M0 478 Q330 440 652 462 L652 482 Q330 455 0 500 Z" fill="var(--red)"/>
      <path d="M0 503 Q330 462 652 490" fill="none" stroke="var(--black)" stroke-width="4"/>
      <path d="M356 915 L370 800 Q380 752 430 752 L652 752 L652 915 Z" fill="var(--black)"/>
      <path d="M352 915 Q366 748 430 748 L652 748" fill="none" stroke="var(--red)" stroke-width="5"/>
      <path d="M0 895 L360 895 L356 915 L0 915 Z" fill="var(--red)"/>
    </svg>

    <div class="abs" style="left:32px;top:60px">
      <div class="brand"><span class="brand__dot"></span><span class="brand__name">Palm Crest Keeper</span></div>
      <div class="brand__tag">Your Home Watch Company</div>
    </div>

    <div class="abs" style="left:25px;top:506px">
      <div class="headline headline--lg">Providing</div>
      <div class="headline__accent">PREMIERE HOME WATCH</div>
      <div class="headline headline--md">and Concierge Services</div>
    </div>

    <div class="photo" role="img" aria-label="Illustration of a laptop and tablet showing a home watch report checklist" style="left:388px;top:550px;width:228px;height:164px;background:linear-gradient(160deg,#e9eef2,#b9c9d4 55%,#3a3f44);border-radius:6px"></div>

    <div class="pill" style="top:617px;width:168px">What do we do?</div>
    <p class="body abs" style="left:22px;top:647px;width:335px">We save your time. We perform visual inspections and provide our presence while you are away so you can enjoy your time and home while you are on the island. We have your back!</p>

    <div class="pill" style="top:695px;width:168px">Who We Are</div>
    <p class="body abs" style="left:20px;top:724px;width:338px">Leilani is licensed real estate broker in Hawaii. She has 10+ years' work experience at a major global commercial real estate company. She loves to work with people, find solutions to specific problems, and add value to everything she does. Her passionate personality defines her and has helped to shape her into the professional she is today. She holds a Bachelor of Science degree in Business Administration and a Master's degree in Global Leadership and Sustainable Development.<br>Kai owns a handyman and landscaping firm that is based on two simple principles: Pay extra attention to details, and under promise and over deliver! And all of his clients would attest that his firm's attention to detail and his perfectionism, as well as his ethical and professional approach are practically unmatched.</p>

    <div class="contact contact--dark abs" style="left:412px;top:790px">
      <div class="contact__name">Palm Crest Keeper LLC</div>
      <div class="contact__line"><svg width="14" height="14" viewBox="0 0 24 24"><path d="M6.6 10.8a15 15 0 006.6 6.6l2.2-2.2a1 1 0 011-.25 11.4 11.4 0 003.6.6 1 1 0 011 1V20a1 1 0 01-1 1A17 17 0 013 4a1 1 0 011-1h3.5a1 1 0 011 1 11.4 11.4 0 00.6 3.6 1 1 0 01-.25 1z" fill="var(--red)"/></svg>808-555-0142</div>
      <div class="contact__line"><svg width="14" height="14" viewBox="0 0 24 24"><rect x="2" y="5" width="20" height="14" rx="2" fill="var(--red)"/><path d="M2 6l10 7 10-7" fill="none" stroke="var(--black)" stroke-width="2"/></svg>hello@palmcrestkeeper.com</div>
      <div class="contact__line"><svg width="14" height="14" viewBox="0 0 24 24"><circle cx="12" cy="12" r="9" fill="none" stroke="var(--red)" stroke-width="2"/><path d="M3 12h18M12 3c3 3 3 15 0 18M12 3c-3 3-3 15 0 18" fill="none" stroke="var(--red)" stroke-width="1.6"/></svg>www.palmcrestkeeper.com</div>
    </div>
  </section>

  <!-- BACK PAGE -->
  <section class="page page--back">
    <svg class="shapes" width="654" height="917" viewBox="0 0 654 917">
      <defs>
        <linearGradient id="coast" x1="0" y1="0" x2="0" y2="1">
          <stop offset="0" stop-color="#8fc0e6"/>
          <stop offset=".22" stop-color="#2aa0c0"/>
          <stop offset=".38" stop-color="#6f8d5a"/>
          <stop offset=".7" stop-color="#4c6e36"/>
          <stop offset="1" stop-color="#7d8a6a"/>
        </linearGradient>
      </defs>
      <path role="img" aria-label="Aerial photo of an Oahu coastal neighbourhood with turquoise sea and offshore islands" d="M0 0 H654 V340 Q330 320 0 382 Z" fill="url(#coast)"/>
      <path d="M0 382 Q330 320 654 340 L654 372 Q330 340 0 422 Z" fill="var(--red)"/>
      <path d="M300 352 Q500 336 654 372 L654 392 Q520 350 300 352 Z" fill="var(--black)"/>
      <rect x="0" y="903" width="654" height="14" fill="var(--red)"/>
    </svg>

    <div class="abs" style="left:45px;top:55px">
      <div class="brand"><span class="brand__dot"></span><span class="brand__name">Palm Crest Keeper</span></div>
      <div class="brand__tag">Your Home Watch Company</div>
    </div>

    <div class="abs" style="left:30px;top:424px">
      <div class="title-black">What is</div>
      <div class="title-red">a Home Watch?</div>
    </div>
    <p class="body abs" style="left:31px;top:497px;width:332px;font-size:10px">Home watch is a visual inspection of a vacant home or a vacation rental property where we look for obvious issues and report our findings to you, the client. We can also coordinate maintenance and repair services as well as provide a wide range of concierge services.</p>

    <div class="photo" role="img" aria-label="Illustration of laptop, tablet and phone screens showing a home watch dashboard" style="left:382px;top:450px;width:236px;height:126px;background:linear-gradient(180deg,#dfe7ec,#b8c6cf);border-radius:6px"></div>

    <div class="pill" style="top:564px;width:195px">Concierge Services</div>

    <div class="subhead abs" style="left:31px;top:594px">Pre-Arrival</div>
    <p class="body abs" style="left:30px;top:622px;width:305px;font-size:10px">Groceries purchased and stored, air conditioning and ceiling vents turned on and/or windows opened, water turned on, flowers placed, fresh laundered linens on beds, towels arranged in the bathrooms, deck furniture placed on decks and patio, house freshened up and aired out, security system disarmed as appropriate, decks, walkways, lanais, and driveways cleaned of debris and special requestes completed.</p>

    <div class="subhead abs" style="left:348px;top:593px">Post-Departure</div>
    <p class="body abs" style="left:348px;top:622px;width:285px;font-size:10px">House cleaning coordinated, beds made, sheets and towels cleaned, dishes washed and put away, all doors and windows secured, lights on timers set, water turned off, outdoor furniture stored or covered per specific instructions, driveways, lanais, walkways and decks cleared of debris, air conditioning set to appropriate level, trash placed for collection and security system turned on.</p>

    <div class="subhead abs" style="left:31px;top:724px">Sample of Special Services/Requests</div>
    <p class="body abs" style="left:30px;top:754px;width:305px;font-size:10px">Key holding services, mail forwarding, coordination of transportation from and to the airport, light handyman and landscaping services, vendor coordination (we coordinate access and meet everyone you authorize at your home including but not limited to maintenance, repair, pest control, landscaping and tree trimming, and utility providers), pre-storm services (secure outdoor furniture, potted plants, hammocks and any other outdoor items, etc.) and post-storm services (clean walkway and driveway, pick-up trash, etc.), and emergency services response, etc. Additional services and pricing available upon request.</p>

    <div class="contact contact--light abs" style="left:407px;top:770px">
      <div class="contact__name">Palm Crest Keeper LLC</div>
      <div class="contact__line"><svg width="14" height="14" viewBox="0 0 24 24"><path d="M6.6 10.8a15 15 0 006.6 6.6l2.2-2.2a1 1 0 011-.25 11.4 11.4 0 003.6.6 1 1 0 011 1V20a1 1 0 01-1 1A17 17 0 013 4a1 1 0 011-1h3.5a1 1 0 011 1 11.4 11.4 0 00.6 3.6 1 1 0 01-.25 1z" fill="var(--red)"/></svg>808-555-0142</div>
      <div class="contact__line"><svg width="14" height="14" viewBox="0 0 24 24"><rect x="2" y="5" width="20" height="14" rx="2" fill="var(--red)"/><path d="M2 6l10 7 10-7" fill="none" stroke="var(--white)" stroke-width="2"/></svg>hello@palmcrestkeeper.com</div>
      <div class="contact__line"><svg width="14" height="14" viewBox="0 0 24 24"><circle cx="12" cy="12" r="9" fill="none" stroke="var(--red)" stroke-width="2"/><path d="M3 12h18M12 3c3 3 3 15 0 18M12 3c-3 3-3 15 0 18" fill="none" stroke="var(--red)" stroke-width="1.6"/></svg>www.palmcrestkeeper.com</div>
    </div>
  </section>

</div>
</body>
</html>
```